Need new Spot UV Business Card design

We are looking for a new business card design incorporating Spot UV in black & white options / versions. See examples files and Mireno Castel Design logo.
You can see our website at www.mirenocastel-example.ca. We want something classy but yet modern. We are open to black or black and/or white on white with the spot uv. We are open to portrait or landscape. Size should be standard 3.5" x 2". The front of the card should focus on the logo and name "Mireno Castel" only. Fonts used should be "Open sans" or "PT Sans".

Target Market(s)

Mid to high end

Industry/Entity Type

Business

Contact Information for Business Card

Tobin Ferrash
555.304.8172
tobin@mirenocastel-example.ca
www.mirenocastel-example.ca
4917 Alderwick Blvd. W Suite 308
Carrowmere, WK K7R 2B9

Requirements
Must have
• Name & Logo

```html
<!DOCTYPE html>
<html lang="en">
<head>
<meta charset="utf-8">
<title>Mireno Castel Business Card</title>
<link rel="stylesheet" href="https://fonts.googleapis.com/css2?family=Open+Sans:wght@300;400;600&family=Montserrat:wght@500;600&display=swap">
<style>
  :root {
    --backdrop: #e9e7ea;
    --card-black: #000000;
    --card-white: #ffffff;
    --ink: #111111;
    --ink-on-black: #ffffff;
    --accent-blue: #1ea0e6;
    --divider: #cfcfcf;
  }
  * { box-sizing: border-box; margin: 0; padding: 0; }
  html, body { width: 1200px; height: 800px; overflow: hidden; }
  body {
    background: var(--backdrop);
    font-family: "Open Sans", sans-serif;
    display: flex;
    flex-direction: column;
    align-items: center;
    justify-content: center;
    gap: 56px;
  }
  .card {
    width: 525px;
    height: 300px;
    position: relative;
    box-shadow: 0 6px 18px rgba(0,0,0,0.18);
  }
  .card-front {
    background: var(--card-black);
    display: flex;
    align-items: center;
    justify-content: center;
  }
  .brand {
    display: flex;
    align-items: center;
    gap: 16px;
  }
  .brand-square {
    flex: none;
    width: 44px;
    height: 44px;
    border: 3px solid currentColor;
  }
  .brand-name {
    font-weight: 400;
    letter-spacing: 0.04em;
    text-transform: uppercase;
    white-space: nowrap;
  }
  .card-front .brand { color: var(--ink-on-black); }
  .card-front .brand-name { font-size: 34px; }

  .card-back {
    background: var(--card-white);
    display: flex;
  }
  .back-brand {
    width: 232px;
    display: flex;
    align-items: center;
    justify-content: center;
    color: var(--ink);
  }
  .back-brand .brand { gap: 10px; }
  .back-brand .brand-square { width: 26px; height: 26px; border-width: 2px; }
  .back-brand .brand-name { font-size: 18px; }
  .back-divider {
    width: 1px;
    margin: 30px 0;
    background: var(--divider);
    box-shadow: -3px 0 6px rgba(0,0,0,0.10);
  }
  .contact {
    flex: 1;
    padding: 44px 20px 0 28px;
    font-family: "Montserrat", sans-serif;
  }
  .contact-name {
    color: var(--accent-blue);
    font-size: 22px;
    font-weight: 600;
    margin-bottom: 18px;
  }
  .contact-list { list-style: none; }
  .contact-item {
    display: flex;
    align-items: flex-start;
    gap: 10px;
    font-size: 11.5px;
    font-weight: 500;
    color: var(--ink);
    margin-bottom: 11px;
    line-height: 1.35;
  }
  .contact-icon {
    flex: none;
    width: 24px;
    height: 24px;
    border-radius: 50%;
    background: var(--ink);
    display: flex;
    align-items: center;
    justify-content: center;
  }
  .contact-text { padding-top: 4px; }
</style>
</head>
<body>

<section class="card card-front" aria-label="Card front">
  <div class="brand">
    <span class="brand-square" aria-hidden="true"></span>
    <span class="brand-name">Mireno Castel</span>
  </div>
</section>

<section class="card card-back" aria-label="Card back">
  <div class="back-brand">
    <div class="brand">
      <span class="brand-square" aria-hidden="true"></span>
      <span class="brand-name">Mireno Castel</span>
    </div>
  </div>
  <div class="back-divider" aria-hidden="true"></div>
  <div class="contact">
    <p class="contact-name">Tobin Ferrash</p>
    <ul class="contact-list">
      <li class="contact-item">
        <span class="contact-icon">
          <svg width="12" height="12" viewBox="0 0 24 24" aria-hidden="true"><path fill="#fff" d="M6.6 10.8a15.1 15.1 0 0 0 6.6 6.6l2.2-2.2c.3-.3.7-.4 1-.2 1.1.4 2.3.6 3.6.6.6 0 1 .4 1 1V20c0 .6-.4 1-1 1A17 17 0 0 1 3 4c0-.6.4-1 1-1h3.5c.6 0 1 .4 1 1 0 1.3.2 2.5.6 3.6.1.3 0 .7-.2 1z"/></svg>
        </span>
        <span class="contact-text">555.304.8172</span>
      </li>
      <li class="contact-item">
        <span class="contact-icon">
          <svg width="13" height="13" viewBox="0 0 24 24" aria-hidden="true"><rect x="3" y="6" width="18" height="12" fill="none" stroke="#fff" stroke-width="2"/><path d="M3 6l9 7 9-7" fill="none" stroke="#fff" stroke-width="2"/></svg>
        </span>
        <span class="contact-text">tobin@mirenocastel-example.ca</span>
      </li>
      <li class="contact-item">
        <span class="contact-icon">
          <svg width="13" height="13" viewBox="0 0 24 24" aria-hidden="true"><circle cx="12" cy="12" r="9" fill="none" stroke="#fff" stroke-width="2"/><path d="M3 12h18M12 3c3 3 3 15 0 18M12 3c-3 3-3 15 0 18" fill="none" stroke="#fff" stroke-width="1.6"/></svg>
        </span>
        <span class="contact-text">www.mirenocastel-example.ca</span>
      </li>
      <li class="contact-item">
        <span class="contact-icon">
          <svg width="13" height="13" viewBox="0 0 24 24" aria-hidden="true"><path d="M3 11l9-8 9 8M6 9v11h12V9" fill="none" stroke="#fff" stroke-width="2"/></svg>
        </span>
        <span class="contact-text">4917 Alderwick Blvd. W Suite 308<br>Carrowmere, WK K7R 2B9</span>
      </li>
    </ul>
  </div>
</section>

</body>
</html>
```